Communication Skill: GLOW Bridge

I need a Design for a skill I teach to youth. That's why the title GLOW Bridge. GLOW stands for Thoughts, Emotions, Concerns, Hopes & Desires. Under each word are some examples that are meant to help people discuss certain things. I tried to create something myself but want something much more creative and dynamic. I have attached what I designed because it has the information I need in the design. Want it to have a techie look to it.

```html
<!DOCTYPE html>
<html lang="en">
<head>
<meta charset="utf-8">
<title>GLOW Bridge – Communication Skill</title>
<link rel="stylesheet" href="https://fonts.googleapis.com/css2?family=Crimson+Pro:wght@400&display=swap">
<style>
  :root {
    --paper: #ffffff;
    --ink: #111111;
    --board: #acadaf;
    --white: #ffffff;
    --thoughts: #f26522;
    --emotions: #9b877b;
    --concerns: #00aeef;
    --hopes: #5677e5;
    --tile-teal: #00b2b0;
    --tile-violet: #6a5fc1;
    --tile-amber: #f7941d;
    --tile-red: #f15a3a;
    --tile-blue: #4b6ee0;
    --tile-green: #7fd14a;
    --figure-warm: #f7a968;
    --figure-orange: #f26522;
  }
  * { margin: 0; padding: 0; box-sizing: border-box; }
  html, body { width: 809px; height: 1200px; overflow: hidden; background: var(--paper); }
  body { position: relative; font-family: "Crimson Pro", Georgia, serif; color: var(--ink); }

  .board {
    position: absolute;
    background: var(--board);
    box-shadow: 4px 8px 10px rgba(0,0,0,0.28);
  }
  .board--portrait { left: 80px; top: 61px; width: 361px; height: 511px; }
  .board--landscape { left: 80px; top: 623px; width: 654px; height: 382px; }

  .board-title {
    position: absolute;
    color: var(--white);
    font-size: 26px;
    font-weight: 400;
    letter-spacing: 1px;
    white-space: nowrap;
    line-height: 1;
  }
  .board--portrait .board-title { left: 0; width: 100%; top: 19px; text-align: center; }
  .board-title--boxed {
    left: 367px; top: 30px; width: 224px; height: 45px;
    border: 1px solid var(--white);
    display: flex; align-items: center; justify-content: center;
  }

  .bubble {
    position: absolute;
    background: var(--c);
    border-radius: 20px;
    color: var(--white);
    text-align: center;
    box-shadow: 2px 4px 5px rgba(0,0,0,0.22);
  }
  .bubble--thoughts { --c: var(--thoughts); }
  .bubble--emotions { --c: var(--emotions); }
  .bubble--concerns { --c: var(--concerns); }
  .bubble--hopes { --c: var(--hopes); }

  .bubble-heading {
    font-size: 32px;
    font-weight: 400;
    line-height: 1;
    margin-top: 7px;
  }
  .bubble-lines {
    font-size: 13px;
    line-height: 16px;
    margin-top: 8px;
    white-space: pre;
  }
  .bubble--emotions .bubble-lines { margin-top: 3px; line-height: 15px; font-size: 12.5px; }
  .tail {
    position: absolute;
    width: 26px; height: 24px;
    fill: var(--c);
    bottom: 12px;
  }
  .tail--left { left: -22px; }
  .tail--right { right: -22px; transform: scaleX(-1); }

  .figure-placeholder {
    position: absolute;
    border-radius: 8px;
    background: linear-gradient(180deg, var(--figure-warm), var(--figure-orange));
    opacity: 0.9;
  }

  .mood-placeholder {
    position: absolute;
    border-radius: 8px;
    background: linear-gradient(135deg, var(--tile-teal), var(--tile-violet) 35%, var(--tile-amber) 55%, var(--tile-red) 70%, var(--tile-blue) 85%, var(--tile-green));
  }

  .product-info { position: absolute; left: 515px; top: 133px; }
  .product-title { font-size: 30px; letter-spacing: 1px; font-weight: 400; white-space: nowrap; }
  .feature-list { position: absolute; left: 34px; top: 76px; list-style: none; font-size: 18px; line-height: 21.5px; white-space: nowrap; }
  .feature-list li.gap { margin-top: 21.5px; }

  .description {
    position: absolute; left: 40px; top: 1068px; width: 729px;
    text-align: center; font-size: 17.5px; line-height: 22px;
  }
</style>
</head>
<body>

<section class="board board--portrait">
  <h1 class="board-title">GLOW&nbsp; BRIDGE</h1>

  <div class="figure-placeholder" style="left:48px;top:63px;width:55px;height:99px;" role="img" aria-label="Illustration: character thinking, with an exclamation mark"></div>
  <div class="bubble bubble--thoughts" style="left:126px;top:63px;width:199px;height:92px;">
    <svg class="tail tail--left" viewBox="0 0 26 24"><path d="M26 0 C20 14 10 20 0 22 C12 24 22 22 26 18 Z"/></svg>
    <h2 class="bubble-heading">Thoughts</h2>
    <p class="bubble-lines">It  seems…          I  wonder…
It’s my opinion…   I believe…</p>
  </div>

  <div class="bubble bubble--emotions" style="left:32px;top:180px;width:163px;height:93px;">
    <svg class="tail tail--right" viewBox="0 0 26 24"><path d="M26 0 C20 14 10 20 0 22 C12 24 22 22 26 18 Z"/></svg>
    <h2 class="bubble-heading">Emotions</h2>
    <p class="bubble-lines">I’m…   hopeful  worried  sad
afraid    mad     glad   happy
confident    insecure</p>
  </div>
  <div class="mood-placeholder" style="left:219px;top:190px;width:109px;height:73px;" role="img" aria-label="Illustration: six coloured emotion face icons"></div>

  <div class="figure-placeholder" style="left:31px;top:285px;width:86px;height:99px;" role="img" aria-label="Illustration: confused character holding head, with a question mark"></div>
  <div class="bubble bubble--concerns" style="left:129px;top:288px;width:199px;height:92px;">
    <svg class="tail tail--left" viewBox="0 0 26 24"><path d="M26 0 C20 14 10 20 0 22 C12 24 22 22 26 18 Z"/></svg>
    <h2 class="bubble-heading">Concerns</h2>
    <p class="bubble-lines">I worry about…   I’m afraid that…
I’m nervous because…</p>
  </div>

  <div class="bubble bubble--hopes" style="left:37px;top:396px;width:199px;height:93px;">
    <svg class="tail tail--right" viewBox="0 0 26 24"><path d="M26 0 C20 14 10 20 0 22 C12 24 22 22 26 18 Z"/></svg>
    <h2 class="bubble-heading">Hopes</h2>
    <p class="bubble-lines">I hope…   I wish…
It’s my desire…   I’d like to see…</p>
  </div>
  <div class="figure-placeholder" style="left:271px;top:392px;width:55px;height:99px;" role="img" aria-label="Illustration: hopeful character with star eyes"></div>
</section>

<aside class="product-info">
  <h2 class="product-title">GLOW&nbsp; BRIDGE</h2>
  <ul class="feature-list">
    <li>High Quality</li>
    <li class="gap">100% Customizable</li>
    <li class="gap">100% Editable</li>
    <li class="gap">Word</li>
    <li>PDF</li>
    <li>PNG</li>
    <li>EPS</li>
    <li>PPT with Animation</li>
    <li class="gap">Convertible any format</li>
  </ul>
</aside>

<section class="board board--landscape">
  <h1 class="board-title board-title--boxed">GLOW&nbsp; BRIDGE</h1>

  <div class="figure-placeholder" style="left:26px;top:77px;width:58px;height:103px;" role="img" aria-label="Illustration: character thinking, with an exclamation mark"></div>
  <div class="bubble bubble--thoughts" style="left:107px;top:76px;width:206px;height:97px;">
    <svg class="tail tail--left" viewBox="0 0 26 24"><path d="M26 0 C20 14 10 20 0 22 C12 24 22 22 26 18 Z"/></svg>
    <h2 class="bubble-heading">Thoughts</h2>
    <p class="bubble-lines">It  seems…          I  wonder…
It’s my opinion…   I believe…</p>
  </div>

  <div class="bubble bubble--emotions" style="left:331px;top:115px;width:169px;height:96px;">
    <svg class="tail tail--right" viewBox="0 0 26 24"><path d="M26 0 C20 14 10 20 0 22 C12 24 22 22 26 18 Z"/></svg>
    <h2 class="bubble-heading">Emotions</h2>
    <p class="bubble-lines">I’m…   hopeful  worried  sad
afraid    mad     glad   happy
confident    insecure</p>
  </div>
  <div class="mood-placeholder" style="left:525px;top:125px;width:114px;height:76px;" role="img" aria-label="Illustration: six coloured emotion face icons"></div>

  <div class="figure-placeholder" style="left:14px;top:213px;width:89px;height:103px;" role="img" aria-label="Illustration: confused character holding head, with a question mark"></div>
  <div class="bubble bubble--concerns" style="left:116px;top:217px;width:205px;height:95px;">
    <svg class="tail tail--left" viewBox="0 0 26 24"><path d="M26 0 C20 14 10 20 0 22 C12 24 22 22 26 18 Z"/></svg>
    <h2 class="bubble-heading">Concerns</h2>
    <p class="bubble-lines">I worry about…   I’m afraid that…
I’m nervous because…</p>
  </div>

  <div class="bubble bubble--hopes" style="left:335px;top:253px;width:207px;height:97px;">
    <svg class="tail tail--right" viewBox="0 0 26 24"><path d="M26 0 C20 14 10 20 0 22 C12 24 22 22 26 18 Z"/></svg>
    <h2 class="bubble-heading">Hopes</h2>
    <p class="bubble-lines">I hope…   I wish…
It’s my desire…   I’d like to see…</p>
  </div>
  <div class="figure-placeholder" style="left:577px;top:249px;width:60px;height:103px;" role="img" aria-label="Illustration: hopeful character with star eyes"></div>
</section>

<p class="description">Lorem ipsum dolor sit amet, consectetuer adipiscing elit, sed diam nonummy nibh euismod tincidunt<br>ut laoreet dolore magna aliquam erat volutpat. Ut wisi enim ad minim veniam, quis nostrud exerci<br>tation ullamcorper suscipit lobortis nisl ut aliquip ex ea</p>

</body>
</html>
```